Unisex deodorant packaging

we need 12 designs of Unisex deodorant spray, all designs shoud be different.

Brand Name is Bremto. Artwork file size is attached for reference. Logo we can be redesigned.

variants names will be:

Pellimore
Quiln
Velontra
Morvik
Zantor
Pluvo
Ryxe
Omber
Sarevin
Tulpo
Vask
Dreen

Target Market(s)

B+, B, C+

Requirements
Must have
• colors, new fonts
Nice to have
• creative work, all 12 designs different

```html
<!DOCTYPE html>
<html lang="en">
<head>
<meta charset="utf-8">
<title>Bremto Zantor – Deodorant Body Spray Box</title>
<link href="https://fonts.googleapis.com/css2?family=Fredoka:wght@500;700&family=Saira+Condensed:wght@500&display=swap" rel="stylesheet">
<style>
  :root {
    --canvas-bg: #ffffff;
    --panel-dark: #120c24;
    --panel-deep: #1c1236;
    --magenta: #a43f9e;
    --magenta-light: #c35bb9;
    --violet-glow: #7a3fc4;
    --pink-glow: #e07ad8;
    --white: #ffffff;
  }
  * { margin: 0; padding: 0; box-sizing: border-box; }
  html, body {
    width: 1126px;
    height: 1200px;
    overflow: hidden;
    background: var(--canvas-bg);
  }
  .canvas {
    position: relative;
    width: 1126px;
    height: 1200px;
    display: flex;
    align-items: center;
    justify-content: center;
  }
  .box-front {
    position: relative;
    width: 560px;
    height: 900px;
    background: linear-gradient(180deg, var(--panel-dark) 0%, var(--panel-deep) 55%, var(--panel-dark) 100%);
    overflow: hidden;
  }
  .band-top, .band-bottom {
    position: absolute;
    left: 0;
    width: 100%;
    height: 16px;
    background: var(--magenta);
  }
  .band-top { top: 0; }
  .band-bottom { bottom: 0; }
  .brand-tab {
    position: absolute;
    top: 0;
    left: 60px;
    width: 290px;
    height: 178px;
    background: var(--magenta);
    border-radius: 0 0 22px 22px;
    display: flex;
    align-items: center;
    justify-content: center;
    gap: 12px;
    padding-top: 30px;
  }
  .brand-dot {
    width: 16px;
    height: 16px;
    border-radius: 50%;
    background: var(--white);
  }
  .brand-name {
    font-family: "Fredoka", sans-serif;
    font-weight: 700;
    font-size: 56px;
    color: var(--white);
    letter-spacing: 1px;
  }
  .variant-name {
    position: absolute;
    top: 300px;
    left: 0;
    width: 100%;
    text-align: center;
    font-family: "Fredoka", sans-serif;
    font-weight: 700;
    font-size: 64px;
    color: var(--magenta-light);
  }
  .light-waves {
    position: absolute;
    left: 0;
    top: 430px;
    width: 100%;
    height: 430px;
    background:
      radial-gradient(ellipse 70% 35% at 65% 45%, rgba(224,122,216,0.55), transparent 70%),
      radial-gradient(ellipse 90% 45% at 40% 70%, rgba(122,63,196,0.5), transparent 75%);
  }
  .product-info {
    position: absolute;
    top: 640px;
    left: 185px;
    width: 170px;
    text-align: center;
    font-family: "Saira Condensed", sans-serif;
    font-weight: 500;
    color: var(--magenta-light);
    font-size: 19px;
    line-height: 1.05;
  }
  .product-info p + p { margin-top: 14px; }
</style>
</head>
<body>
  <main class="canvas">
    <section class="box-front">
      <div class="band-top"></div>
      <div class="brand-tab">
        <span class="brand-dot"></span>
        <span class="brand-name">BREMTO</span>
      </div>
      <h1 class="variant-name">Zantor</h1>
      <div class="light-waves" role="img" aria-label="Flowing violet and pink light wave streaks"></div>
      <div class="product-info">
        <p>French<br>Perfumed</p>
        <p>Deodorant<br>Body Spray</p>
        <p>150ml Net: 5.1 fl.oz.</p>
      </div>
      <div class="band-bottom"></div>
    </section>
  </main>
</body>
</html>
```